CPA Graduation Party

I need to make simple invitation for my sister's recent success, passing the CPA (Certified Public Accountant) exam. It is a surprise party. I want very simple and professional looking invitation. My only requirements are that you don't use any graduation caps or gowns due to the fact that it's not an actual graduation. It's a series of exams that she passes. Be creative with the design but once again, keep it professional. I have attached a font called iScriptSTD. I liked the font so was thinking about using it. But it's not necessary. If you have something slimier or better, please use it.

I was planning on printing on a specific kind of paper. It's called pearlized ivory cardstock. It has a little coating and shine on it and since it's ivory, I was thinking about the main color of the invitation to be burgundy type. For example, see the following RGB: R204, G0, B102.

Party info:
Name: Ravina
Date & Time: Saturday, March 8th, 2014 at 6:00pm
Location: Seher Mahal. 418 Brambleford Lane Larkhaven, NE 07291

I know I didn't provide a lot of info for the invite but please be creative.  Use general knowledge and other formal party invites as examples. I am not looking for a name, date and location as three bullets on the card.

Also, I forgot to mention the size of the invite.  It should be 5.5x8.5.  Thank you.

• graduation caps and/or gowns

```html
<!DOCTYPE html>
<html lang="en">
<head>
<meta charset="utf-8">
<title>Ravina's Celebration Party Invitation</title>
<link rel="stylesheet" href="https://fonts.googleapis.com/css2?family=Aladin&family=Tinos&display=swap">
<style>
  :root {
    --page: #ffffff;
    --card: #f0f0f0;
    --berry: #cc0066;
    --rule: #c8c8c8;
  }
  html, body {
    margin: 0;
    padding: 0;
    width: 1200px;
    height: 1000px;
    overflow: hidden;
    background: var(--page);
  }
  .invitation {
    position: absolute;
    left: 117px;
    top: 177px;
    width: 958px;
    height: 620px;
    background: var(--card);
    overflow: hidden;
    font-family: "Tinos", "Times New Roman", serif;
    color: var(--berry);
    text-align: center;
  }
  .ornament {
    position: absolute;
    display: block;
  }
  .ornament--top {
    left: 275px;
    top: 0;
  }
  .ornament--bottom {
    left: 303px;
    top: 543px;
  }
  .line {
    position: absolute;
    left: 0;
    width: 100%;
    margin: 0;
    font-weight: 400;
  }
  .kicker {
    font-size: 17px;
    letter-spacing: 0.2px;
  }
  .kicker--invited { top: 175px; }
  .kicker--party { top: 308px; }
  .kicker--venue { top: 398px; }
  .guest-name {
    top: 192px;
    font-family: "Aladin", cursive;
    font-size: 104px;
    line-height: 1.1;
    font-style: italic;
  }
  .divider {
    position: absolute;
    left: 288px;
    top: 358px;
    display: block;
  }
  .details {
    top: 446px;
    font-size: 17px;
    line-height: 26px;
  }
</style>
</head>
<body>
  <main class="invitation">
    <svg class="ornament ornament--top" width="408" height="134" viewBox="0 0 408 134" role="img" aria-label="Symmetrical magenta paisley and swirl ornament">
      <path d="M0 0 H408 V30 Q408 70 360 88 Q300 100 260 128 Q204 140 148 128 Q108 100 48 88 Q0 70 0 30 Z" fill="var(--berry)"/>
    </svg>

    <p class="line kicker kicker--invited">YOU ARE INVITED TO</p>
    <h1 class="line guest-name">Ravina’s</h1>
    <p class="line kicker kicker--party">CELERATION PARTY</p>

    <svg class="divider" width="384" height="20" viewBox="0 0 384 20" aria-hidden="true">
      <line x1="0" y1="10.5" x2="384" y2="10.5" stroke="var(--rule)" stroke-width="1"/>
      <path d="M189.5 0 L195.5 9.5 L189.5 19 L183.5 9.5 Z" fill="var(--berry)"/>
    </svg>

    <p class="line kicker kicker--venue">THE PARTY WILL BE HELD AT</p>
    <p class="line details">Seher Mahal. 418 Brambleford Lane Larkhaven, NE 07291<br>on Saturday, April 12th, 2014 at 7.00pm</p>

    <svg class="ornament ornament--bottom" width="352" height="77" viewBox="0 0 352 77" role="img" aria-label="Symmetrical magenta paisley and swirl ornament">
      <path d="M0 77 V60 Q10 44 40 44 Q70 30 100 10 Q140 0 176 4 Q212 0 252 10 Q282 30 312 44 Q342 44 352 60 V77 Z" fill="var(--berry)"/>
    </svg>
  </main>
</body>
</html>
```